Brume d'Orvelle Hand Crafted Candles promotional flyer

Hand Crafted Soy Candles - I need a flyer to promote my candles and to give information on care of candles.I want this to use the design and colours I already have for my labels and the photo I have attached.I am aiming at a sophisticated market so would like to reflect this in the design.
Should appeal to sophisticated women who enjoy the pleasure of candles - to enhance their enjoyment of life - gives them the 'brume d'orvelle'.
the candles are hand crafted from all natural ingredients, environmentally friendly and with exquisite fragrances

Target Market(s)

sophisticated females

Industry/Entity Type

Promotional

Font styles to use
Script

Colors
cfeae6
ecdaeb

Requirements
Must have
• something expressing 'brume d'orvelle' - the enjoyment of candles
Should not have
• bright colours

```html
<!DOCTYPE html>
<html lang="en">
<head>
<meta charset="utf-8">
<title>Brume d'Orvelle Hand Crafted Candles</title>
<link href="https://fonts.googleapis.com/css2?family=Pinyon+Script&family=Questrial&display=swap" rel="stylesheet">
<style>
  :root {
    --stage: #3b3b3d;
    --blush: #ecdaeb;
    --mint: #cfeae6;
    --mint-pale: #deefed;
    --ink: #1f1f1f;
    --ink-soft: #2e2e2e;
    --silver-light: #f4f4f6;
    --silver-dark: #8d8e93;
    --candle-dark: #1c1c22;
  }
  * { margin: 0; padding: 0; box-sizing: border-box; }
  html, body { width: 900px; height: 1200px; overflow: hidden; }
  body { background: var(--stage); position: relative; font-family: "Questrial", "Century Gothic", sans-serif; color: var(--ink); }

  .flyer { position: absolute; left: 50px; top: 38px; width: 800px; height: 1124px; overflow: hidden; background: var(--blush); }
  .flyer-shapes { position: absolute; inset: 0; }

  .brand-seal { position: absolute; left: 34px; top: 12px; width: 234px; height: 234px; border-radius: 50%;
    background: radial-gradient(circle, #e8f5f3 0%, var(--mint-pale) 70%, #c9e3e0 100%);
    display: flex; align-items: center; justify-content: center; }
  .brand-seal-name { font-family: "Pinyon Script", cursive; font-size: 40px; color: var(--ink-soft); }

  .title { position: absolute; left: 360px; top: 20px; width: 430px; text-align: center;
    font-family: "Pinyon Script", cursive; font-size: 62px; line-height: 1; color: var(--ink); }
  .tagline { position: absolute; left: 360px; top: 100px; width: 430px; text-align: center;
    font-family: "Pinyon Script", cursive; font-size: 31px; color: var(--ink); }

  .section-heading { position: absolute; font-family: "Pinyon Script", cursive; color: var(--ink); }
  .about-heading { left: 76px; top: 356px; font-size: 32px; }
  .soy-heading { left: 70px; top: 553px; font-size: 32px; }
  .care-heading { left: 472px; top: 262px; font-size: 28px; }

  .copy { position: absolute; list-style: none; }
  .copy li { margin: 0; }
  .about-list { left: 40px; top: 402px; width: 330px; font-size: 14.2px; line-height: 16.6px; }
  .soy-list { left: 40px; top: 608px; width: 330px; font-size: 14.6px; line-height: 16.9px; }
  .care-list { left: 437px; top: 318px; width: 345px; font-size: 12.8px; line-height: 16.6px; }

  .contact { position: absolute; left: 40px; top: 1008px; list-style: none; font-size: 19px; line-height: 26px; color: var(--ink); }
  .contact li { display: flex; align-items: center; gap: 10px; }
  .contact svg { width: 14px; height: 14px; flex: none; }

  .candle-photo { position: absolute; left: 568px; top: 948px; width: 176px; height: 176px; border-radius: 12px 12px 0 0;
    background: radial-gradient(ellipse at 40% 35%, #3a3a44 0%, var(--candle-dark) 65%); }
</style>
</head>
<body>
  <main class="flyer">
    <svg class="flyer-shapes" viewBox="0 0 800 1124" width="800" height="1124" aria-hidden="true">
      <defs>
        <linearGradient id="silver" x1="0" y1="0" x2="1" y2="1">
          <stop offset="0" stop-color="var(--silver-dark)"/>
          <stop offset="0.45" stop-color="var(--silver-light)"/>
          <stop offset="1" stop-color="var(--silver-dark)"/>
        </linearGradient>
      </defs>
      <path d="M0,345 C120,350 230,300 340,245 C470,185 640,168 800,165 L800,1124 L0,1124 Z" fill="var(--mint)"/>
      <path d="M0,1000 C180,985 380,990 560,1010 L560,1124 L0,1124 Z" fill="var(--blush)"/>
      <path d="M6,1000 C180,985 380,990 540,1006" fill="none" stroke="url(#silver)" stroke-width="6"/>
      <circle cx="151" cy="129" r="135" fill="none" stroke="url(#silver)" stroke-width="12"/>
      <path d="M30,300 C110,360 230,320 340,245 C470,185 640,168 800,162" fill="none" stroke="url(#silver)" stroke-width="12"/>
      <circle cx="656" cy="1045" r="140" fill="var(--mint-pale)"/>
      <circle cx="656" cy="1045" r="146" fill="none" stroke="url(#silver)" stroke-width="12"/>
    </svg>

    <div class="brand-seal"><span class="brand-seal-name">Brume d'Orvelle</span></div>

    <h1 class="title">Brume d'Orvelle</h1>
    <p class="tagline">an exuberant enjoyment of life</p>

    <h2 class="section-heading about-heading">About Us</h2>
    <ul class="copy about-list">
      <li>• Brume d'Orvelle – an exuberant enjoyment of life – these candles will fill you with “Brume d'Orvelle”.</li>
      <li>• Candles are lovingly hand-poured and use only the finest of ingredients and fragrances</li>
      <li>• Hand crafted soy candle creations</li>
      <li>• Completely non-toxic</li>
      <li>• Exquisite fragrances</li>
      <li>• Clean burning</li>
      <li>• Environmentally friendly.</li>
    </ul>

    <h2 class="section-heading soy-heading">Why soy wax?</h2>
    <ul class="copy soy-list">
      <li>• Soft smooth wax that burns clear – no soot or smoke</li>
      <li>• Soy wax candles burn up to 50% longer than traditional paraffin candles</li>
      <li>• Made from soya beans, a renewable natural resource that supports and sustains agriculture – it is biodegradable and environmentally friendly.</li>
      <li>• Soy wax burns cooler than paraffin and disperse the fragrance more fully.</li>
      <li>Containers can be refilled</li>
      <li>• I offer a refill service - if you return your containers to me I can refill with the fragrance of your choice</li>
      <li>• Or if you have a special container you would like to use for your candle just contact me for a quote.</li>
      <li>• I have a wide range of fragrances - please contact me for details.</li>
    </ul>

    <h2 class="section-heading care-heading">How to care for your candle</h2>
    <ul class="copy care-list">
      <li>The following tips will ensure you have a long lasting, fully fragranced candle</li>
      <li>• When lighting your candle for the first time, allow the wax to melt all the way to the sides of the container – this creates a ‘memory’ and avoids ‘tunnelling’ as the candle burns.</li>
      <li>• Always trim the wick to about 6-8mm before re-lighting your candle. This will ensure a long lasting candle, minimise soot and remove any mushrooming of the wick from a previous burn.</li>
      <li>• It is preferable to use a candle ‘snuffer’ to extinguish the flame, or a lid if the candle has one. Alternatively, you can dip the wick into the melted wax and then straightening. This will stop the wick from smoking and help with relighting.</li>
      <li>• All Brume d'Orvelle candles are hand poured not massed produced – although every effort is made to ensure consistency, every candle may be different.</li>
      <li>• Sometimes you may notice darker patches or wet spots - this is not a fault it is just the natural way the wax has set – it does not affect the candle in anyway.</li>
      <li>• The top of the candle may also appear slightly uneven – this is just a sign of natural soy wax being hand poured.</li>
      <li>• Do not leave your candle in the sunlight as it may turn a yellow colour – again this does not affect the candle in anyway – it just loses its creamy white colour.</li>
      <li>• As these candles contain no preservatives or chemicals it is recommended that they should be used within 6 months.</li>
    </ul>

    <ul class="contact">
      <li><svg viewBox="0 0 14 14"><rect x="1" y="3" width="12" height="8" fill="none" stroke="#333" stroke-width="1.4"/><path d="M1,3 L7,8 L13,3" fill="none" stroke="#333" stroke-width="1.4"/></svg>odile.marchant@mailbox.co.nz</li>
      <li><svg viewBox="0 0 14 14"><rect x="3.5" y="0.5" width="7" height="13" rx="1.2" fill="#333"/><rect x="5" y="2.5" width="4" height="4" fill="#ddd"/></svg>021 555 0184</li>
      <li><svg viewBox="0 0 14 14"><circle cx="7" cy="7" r="6" fill="none" stroke="#333" stroke-width="1.4"/><path d="M1,7 H13 M7,1 C4,4 4,10 7,13 M7,1 C10,4 10,10 7,13" fill="none" stroke="#333" stroke-width="1"/></svg>www.mybrumedorvelle.co.nz</li>
    </ul>

    <div class="candle-photo" role="img" aria-label="Photo of a black glass candle jar with the Brume d'Orvelle label"></div>
  </main>
</body>
</html>
```